Retail Sign for Houseplant Campaign

Please make Portrait style not landscape Sign will measure 3 to 4 foot tall by 22.2inches and place on rolling racks of houseplants for a retail promotion in The Yard Locker. The theme of the promotion will be "Bring your home to life with Houseplants!" Selling points which should be on the sign are Houseplants * improve your mood * reduce fatigue * improve focus. Please put signage in landscape format and include yard locker and verdant makings logo.

Just recovered from covid. Im sorry for the delay

Target Market(s)

People who love plants

Industry/Entity Type

Retail

Colors
00AB8E
00BBA5
67D7C9
C6EFE9
E9F9F6
59FF00
82FF00
B8FF75
E3FFCB
F4FFEA
FFF300
FFF600
FEFA6F
FFFEC7
FFFEE8
FFC000
F8CF3A
FAE287
FDF2CF
FEFAEE

Requirements
Must have
• Must feel energetic and encourage people to buy plants. Should include 1-2 photos and the selling points listed

```html
<!DOCTYPE html>
<html lang="en">
<head>
<meta charset="utf-8">
<title>Bring Your Home to Life with Houseplants</title>
<link href="https://fonts.googleapis.com/css2?family=Montserrat:wght@600;800;900&family=Questrial&display=swap" rel="stylesheet">
<style>
  :root{
    --leaf-bg:#b5d274;
    --leaf-soft:#c6de8c;
    --leaf-deep:#9fc35f;
    --leaf-dark:#5a6e2f;
    --panel-green:#45972f;
    --orange:#e96b1c;
    --amber:#f29a1c;
    --coral:#ee5a3a;
    --sun:#f5e816;
    --tick:#5fe01c;
    --white:#ffffff;
  }
  html,body{margin:0;padding:0;overflow:hidden;}
  body{width:1200px;height:2554px;background:var(--leaf-bg);}
  .sign{display:block;width:1200px;height:2554px;}
  .headline{font-family:"Montserrat",sans-serif;font-weight:900;paint-order:stroke;stroke:var(--white);stroke-linejoin:round;}
  .headline--bring{fill:var(--orange);stroke-width:14;}
  .headline--your{fill:var(--leaf-dark);stroke-width:0;}
  .headline--home{fill:var(--sun);stroke-width:0;}
  .headline--life{fill:var(--white);stroke-width:0;}
  .headline--plants{fill:var(--amber);stroke-width:14;}
  .ribbon-title{font-family:"Montserrat",sans-serif;font-weight:600;fill:var(--white);}
  .benefit{font-family:"Questrial",sans-serif;fill:var(--white);}
  .brand-text{font-family:"Questrial",sans-serif;fill:var(--white);}
  .maker-name{font-family:"Questrial",sans-serif;fill:var(--leaf-dark);}
</style>
</head>
<body>
<svg class="sign" viewBox="0 0 1200 2554" xmlns="http://www.w3.org/2000/svg">
  <defs>
    <linearGradient id="bg-wash" x1="0" y1="0" x2="1" y2="1">
      <stop offset="0" stop-color="#b9d577"/>
      <stop offset="1" stop-color="#afcd6d"/>
    </linearGradient>
    <radialGradient id="leaf-glow" cx="0.5" cy="0.5" r="0.5">
      <stop offset="0" stop-color="#cfe49a" stop-opacity="0.95"/>
      <stop offset="0.7" stop-color="#c3dc88" stop-opacity="0.6"/>
      <stop offset="1" stop-color="#b5d274" stop-opacity="0"/>
    </radialGradient>
    <radialGradient id="leaf-shade" cx="0.5" cy="0.5" r="0.5">
      <stop offset="0" stop-color="#93bb55" stop-opacity="0.75"/>
      <stop offset="1" stop-color="#b5d274" stop-opacity="0"/>
    </radialGradient>
    <linearGradient id="photo-wall" x1="0" y1="0" x2="1" y2="0">
      <stop offset="0" stop-color="#f3ea80"/>
      <stop offset="1" stop-color="#f1e56e"/>
    </linearGradient>
    <radialGradient id="photo-palms" cx="0.25" cy="0.85" r="0.7">
      <stop offset="0" stop-color="#2f5a1f" stop-opacity="0.85"/>
      <stop offset="0.6" stop-color="#4f7d2c" stop-opacity="0.45"/>
      <stop offset="1" stop-color="#4f7d2c" stop-opacity="0"/>
    </radialGradient>
    <radialGradient id="photo-subject" cx="0.78" cy="0.45" r="0.45">
      <stop offset="0" stop-color="#e8b79c" stop-opacity="0.9"/>
      <stop offset="0.55" stop-color="#c98a6a" stop-opacity="0.55"/>
      <stop offset="1" stop-color="#c98a6a" stop-opacity="0"/>
    </radialGradient>
    <clipPath id="photo-clip">
      <path d="M545 2554 C560 2150 780 1760 1200 1565 L1200 2554 Z"/>
    </clipPath>
  </defs>

  <!-- background -->
  <rect class="backdrop" width="1200" height="2554" fill="url(#bg-wash)"/>

  <!-- foliage backdrop -->
  <g class="foliage-backdrop" role="img" aria-label="Soft background of pale tropical monstera and palm leaves">
    <ellipse cx="1000" cy="170" rx="330" ry="290" fill="url(#leaf-glow)"/>
    <ellipse cx="1120" cy="330" rx="200" ry="260" fill="url(#leaf-shade)"/>
    <ellipse cx="1130" cy="1040" rx="180" ry="260" fill="url(#leaf-glow)"/>
    <ellipse cx="130" cy="1100" rx="260" ry="330" fill="url(#leaf-shade)"/>
    <ellipse cx="250" cy="1480" rx="330" ry="300" fill="url(#leaf-glow)"/>
    <ellipse cx="120" cy="1900" rx="240" ry="230" fill="url(#leaf-glow)"/>
    <ellipse cx="1120" cy="660" rx="160" ry="180" fill="url(#leaf-glow)"/>
  </g>

  <!-- store name -->
  <g class="store-name">
    <text class="brand-text" x="1040" y="150" font-size="44" text-anchor="middle">The Yard</text>
    <text class="brand-text" x="1040" y="202" font-size="44" text-anchor="middle">Locker</text>
  </g>

  <!-- headline -->
  <g class="headline-group">
    <text class="headline headline--bring" x="112" y="285" font-size="236" textLength="660" lengthAdjust="spacingAndGlyphs">BRING</text>
    <text class="headline headline--your" x="100" y="443" font-size="182" textLength="493" lengthAdjust="spacingAndGlyphs">YOUR</text>
    <text class="headline headline--home" x="648" y="443" font-size="182" textLength="465" lengthAdjust="spacingAndGlyphs">HOME</text>
    <text class="headline headline--life" x="80" y="615" font-size="183" textLength="1035" lengthAdjust="spacingAndGlyphs">TO LIFE WITH</text>
    <text class="headline headline--plants" x="105" y="765" font-size="160" textLength="1013" lengthAdjust="spacingAndGlyphs">HOUSEPLANTS!</text>
  </g>

  <!-- benefits panel -->
  <g class="benefits-panel">
    <polygon points="142,945 818,870 953,1298 203,1418" fill="var(--panel-green)" stroke="var(--white)" stroke-width="10" stroke-linejoin="round"/>
    <polygon points="112,1012 120,1170 150,1165" fill="var(--coral)"/>
    <polygon points="885,908 922,1065 935,1062" fill="var(--coral)"/>
    <polygon points="112,1012 885,908 922,1065 142,1162" fill="var(--orange)"/>
    <text class="ribbon-title" x="515" y="1080" font-size="88" text-anchor="middle" transform="rotate(-7.5 515 1050)" textLength="690" lengthAdjust="spacingAndGlyphs">HOUSEPLANTS</text>

    <g class="benefit-line" transform="rotate(-7 520 1220)">
      <path d="M202 1182 l22 34 l54 -78" fill="none" stroke="var(--tick)" stroke-width="16" stroke-linecap="round" stroke-linejoin="round"/>
      <text class="benefit" x="282" y="1215" font-size="70" textLength="588" lengthAdjust="spacingAndGlyphs">improve your mood</text>
    </g>
    <g class="benefit-line" transform="rotate(-7 520 1310)">
      <path d="M228 1280 l22 34 l54 -78" fill="none" stroke="var(--tick)" stroke-width="16" stroke-linecap="round" stroke-linejoin="round"/>
      <text class="benefit" x="308" y="1313" font-size="74" textLength="505" lengthAdjust="spacingAndGlyphs">reduce  fatigue</text>
    </g>
  </g>

  <!-- focus tag -->
  <g class="focus-tag">
    <polygon points="765,1590 900,1560 880,1720" fill="var(--coral)"/>
    <polygon points="327,1462 900,1422 915,1560 333,1650" fill="var(--amber)" stroke="var(--white)" stroke-width="10" stroke-linejoin="round"/>
    <g transform="rotate(-5 620 1545)">
      <path d="M355 1530 l22 34 l54 -78" fill="none" stroke="var(--tick)" stroke-width="16" stroke-linecap="round" stroke-linejoin="round"/>
      <text class="benefit" x="430" y="1565" font-size="68" textLength="445" lengthAdjust="spacingAndGlyphs">improve  focus</text>
    </g>
  </g>

  <!-- accent shapes -->
  <g class="accents">
    <polygon points="960,1210 1000,1195 975,1250" fill="var(--amber)"/>
    <polygon points="915,1330 995,1345 955,1415" fill="var(--orange)"/>
    <polygon points="912,1400 955,1455 915,1455" fill="var(--panel-green)"/>
    <circle cx="928" cy="1520" r="7" fill="var(--panel-green)"/>
    <polygon points="242,1790 295,1790 245,1870" fill="var(--orange)"/>
    <polygon points="175,1940 290,1950 205,2010" fill="var(--orange)"/>
    <polygon points="180,1960 250,1985 185,2005" fill="var(--amber)"/>
    <circle cx="128" cy="1855" r="9" fill="var(--orange)"/>
    <circle cx="178" cy="1862" r="20" fill="var(--amber)"/>
  </g>

  <!-- photo -->
  <g class="photo-frame">
    <path d="M485 2554 C495 2110 760 1640 1160 1450 L1200 1440 L1200 2554 Z" fill="var(--leaf-dark)"/>
    <g class="photo" clip-path="url(#photo-clip)" role="img" aria-label="Photo of a smiling woman in sunglasses peeking through palm leaves against a yellow wall">
      <rect x="540" y="1560" width="660" height="994" fill="url(#photo-wall)"/>
      <rect x="540" y="1560" width="660" height="994" fill="url(#photo-palms)"/>
      <rect x="540" y="1560" width="660" height="994" fill="url(#photo-subject)"/>
    </g>
  </g>

  <!-- maker name -->
  <g class="maker-badge">
    <rect x="-40" y="2092" width="655" height="230" rx="50" fill="var(--white)" stroke="var(--leaf-dark)" stroke-width="14"/>
    <rect x="48" y="2165" width="100" height="100" fill="var(--leaf-dark)"/>
    <text class="maker-name" x="178" y="2235" font-size="80" textLength="385" lengthAdjust="spacingAndGlyphs">VERDANT</text>
    <text class="maker-name" x="182" y="2270" font-size="32" textLength="375" lengthAdjust="spacing" letter-spacing="14">MAKINGS</text>
  </g>
</svg>
</body>
</html>
```